Marovan Lawyers needs a logo, business cards and stationery

we are a law firm that is new, progressive, energetic whilst still maintaining traditional values of the law. Our logo is attached. The square in the logo can be positioned above the name if required. The blue in the logo should be closer to a pantone PMS 2995 colour. Need business cards and letterhead and envelopes and with compliments slip. There is a separate contest for the business cards.
The business card should be double sided and i am looking to have a QR code either on the front or the back with contact information.
If you think you can do more with the logo, let me know.

The firm name is Marovan Lawyers

Reason: Contest went offline for a day, and other contest failed to launch. Need more time to consider designs

Industry/Entity Type

Business

Font styles to use
Sans Serif

Colors
33a6d7

Requirements
Must have
• The stationery needs to have the firm name
• The physical address and a postal address
• webpage
Should not have
• Avoid any legal type images such as scales and columns etc, they seem to be overdone

```html
<!DOCTYPE html>
<html lang="en">
<head>
<meta charset="utf-8">
<title>Marovan Lawyers – With Compliments Slip</title>
<link rel="stylesheet" href="https://fonts.googleapis.com/css2?family=Didact+Gothic&family=Pinyon+Script&display=swap">
<style>
  :root {
    --backdrop: #5e5e5e;
    --paper: #ffffff;
    --brand-blue: #0d4c82;
    --ink: #3a3a3a;
    --charcoal: #333333;
    --rule: #bdbdbd;
  }
  * { margin: 0; padding: 0; box-sizing: border-box; }
  html, body {
    width: 1200px; height: 1000px; overflow: hidden;
    background: var(--backdrop);
  }
  .slip {
    position: absolute; left: 147px; top: 299px;
    width: 893px; height: 421px;
    background: var(--paper);
    box-shadow: 2px 3px 6px rgba(0,0,0,0.35);
  }
  .brand {
    position: absolute; left: 55px; top: 56px;
    display: flex; align-items: flex-start; gap: 8px;
    color: var(--brand-blue);
    font-family: "Didact Gothic", sans-serif;
  }
  .brand-square {
    width: 50px; height: 50px; background: var(--brand-blue);
  }
  .brand-name { line-height: 1; }
  .brand-name .firm { display: block; font-size: 41px; letter-spacing: 1px; margin-top: -3px; }
  .brand-name .kind { display: block; font-size: 14px; letter-spacing: 13.5px; margin-top: 1px; }
  .contact {
    position: absolute; left: 51px; top: 341px;
    display: flex; font-family: "Didact Gothic", sans-serif;
    font-size: 12px; color: var(--ink); line-height: 18px;
  }
  .contact .label { color: var(--brand-blue); font-weight: bold; }
  .contact .postal { padding-right: 18px; border-right: 1px solid var(--rule); }
  .contact .lines { padding-left: 18px; }
  .greeting {
    position: absolute; left: 493px; top: 316px;
    font-family: "Pinyon Script", cursive;
    font-size: 44px; white-space: nowrap;
  }
  .greeting .with { color: var(--ink); }
  .greeting .compliments { color: var(--brand-blue); }
  .band {
    position: absolute; bottom: 0; left: 0; width: 100%; height: 14px;
  }
</style>
</head>
<body>
  <div class="slip">
    <div class="brand">
      <div class="brand-square"></div>
      <div class="brand-name">
        <span class="firm">MAROVAN</span>
        <span class="kind">LAWYERS</span>
      </div>
    </div>

    <div class="contact">
      <div class="postal">
        <div>P.O Box 4120, Elmridge, Victoria 3182</div>
        <div><span class="label">W:</span> www.marovanlawyers.com.au</div>
      </div>
      <div class="lines">
        <div><span class="label">T:</span> +61 3 9471 2200</div>
        <div><span class="label">F:</span> +61 3 9471 2201</div>
      </div>
    </div>

    <div class="greeting"><span class="with">With</span> <span class="compliments">Compliments</span></div>

    <svg class="band" viewBox="0 0 893 14" preserveAspectRatio="none" aria-hidden="true">
      <rect x="0" y="0" width="456" height="14" fill="var(--brand-blue)"/>
      <rect x="460" y="0" width="433" height="14" fill="var(--charcoal)"/>
    </svg>
  </div>
</body>
</html>
```